Premium modern eliquids labels 84.5 x 80 mm

I am looking for modern graphics for the labels of a new eliquid line that will have 4 different types of eliquids. It will have a tobacco one (brown colours maybe), a fruity one (bright colours maybe), a minty one (green colours maybe) and a creamy one (beige colours maybe).
I will need one of them to see how the design is, that design will have to be adapted to the other 3 colours of the label.
The brand logo is attached. I also attached a sample of what is mandatory to write on the label, you can change size, place and font of what is written, the only thing that cannot be reduced is the yellow parts. I attach the bottle that we will use.The size of the label is 84.5 x 80 mm (base x height).

Target Market(s)

vapers

Requirements
Must have
• My project must have one of the labels.

```html
<!DOCTYPE html>
<html lang="it">
<head>
<meta charset="utf-8">
<title>Pure Vapour – Mystic Mint label</title>
<link rel="stylesheet" href="https://fonts.googleapis.com/css2?family=Roboto:wght@400;500;700;900&family=Great+Vibes&display=swap">
<style>
  :root {
    --label-green: #0d4a22;
    --label-green-deep: #0a3f1c;
    --ink: #ffffff;
    --brand-blue: #72b8e6;
    --badge-yellow: #f6b500;
    --leaf-light: #c9e25a;
    --leaf-dark: #4f9a2a;
  }
  * { margin: 0; padding: 0; box-sizing: border-box; }
  html, body { width: 1200px; height: 1137px; overflow: hidden; }
  body {
    background: var(--label-green);
    font-family: "Roboto", Arial, sans-serif;
    color: var(--ink);
  }
  .label {
    position: relative;
    width: 1200px; height: 1137px;
    background: radial-gradient(ellipse at 50% 45%, var(--label-green) 0%, var(--label-green-deep) 100%);
  }
  .block { position: absolute; font-size: 20.5px; line-height: 29px; }
  .ingredients { left: 17px; top: 58px; }
  .batch { left: 17px; top: 366px; }
  .producer { left: 17px; top: 861px; }
  .usage { left: 876px; top: 58px; font-weight: 500; }

  .brand {
    position: absolute; left: 340px; top: 200px; width: 520px;
    display: flex; align-items: center; justify-content: center; gap: 14px;
    white-space: nowrap;
    color: var(--brand-blue); font-weight: 900; font-size: 54px; line-height: 1; letter-spacing: 2px;
  }
  .brand-dot { flex: none; width: 22px; height: 22px; border-radius: 50%; background: var(--brand-blue); }
  .category {
    position: absolute; left: 398px; top: 378px; width: 400px; text-align: center;
    font-weight: 700; font-size: 42px;
  }
  .hero-art {
    position: absolute; left: 421px; top: 722px; width: 356px; height: 230px;
    border-radius: 50% 50% 45% 45%;
    background: radial-gradient(ellipse at 50% 50%, var(--leaf-light) 0%, var(--leaf-dark) 80%, transparent 100%);
  }
  .flavour-name {
    position: absolute; left: 348px; top: 1010px; width: 500px; text-align: center;
    font-family: "Great Vibes", cursive; font-size: 64px; line-height: 1;
  }

  .more-title { position: absolute; left: 873px; top: 302px; font-size: 20.5px; font-weight: 700; }
  .flavour-art { position: absolute; border-radius: 40%; }
  .art-fruity { left: 849px; top: 351px; width: 204px; height: 72px;
    background: linear-gradient(90deg, #f2c12e, #e2572a, #f08a2a, #9cc23a); }
  .art-tobacco { left: 893px; top: 445px; width: 112px; height: 104px;
    background: radial-gradient(ellipse, #dfe2a6, #9aa15c); }
  .art-vanilla { left: 836px; top: 575px; width: 229px; height: 90px;
    background: linear-gradient(90deg, #4a2a1c, #f2d23c 50%, #4a2a1c); }
  .flavour-label {
    position: absolute; text-align: center;
    font-size: 20.5px; line-height: 29px; font-weight: 500;
  }
  .label-fruity { top: 358px; right: 36px; }
  .label-tobacco { top: 485px; right: 24px; }
  .label-vanilla { top: 588px; right: 18px; }

  .badge {
    position: absolute; background: var(--badge-yellow); border-radius: 10px;
    display: flex; align-items: center; justify-content: center; text-align: center;
    font-weight: 500;
  }
  .badge-collect { left: 869px; width: 160px; height: 60px; font-size: 19px; line-height: 22px; }
  .badge-code { left: 1041px; width: 133px; height: 50px; font-size: 32px; font-weight: 700; }
  .part { position: absolute; left: 1047px; font-size: 20.5px; }
  .volume { position: absolute; left: 879px; top: 982px; font-size: 26px; font-weight: 700; }
  .icon { position: absolute; }
</style>
</head>
<body>
<main class="label">
  <p class="block ingredients">INGREDIENTI:<br>GLICOLE, PROPILENICO<br>SOSTANZE, AROMATIZZANTI</p>

  <div class="brand"><span class="brand-dot"></span><span>PURE VAPOUR</span></div>
  <p class="category">eliquids</p>

  <p class="block usage">ISTRUZIONI D’USO:<br>Agitare bene prima<br>dell’utilizzo.<br>Diluire nelle percentuali<br>consigliate sul nostro sito.<br>Conservare in luogo fresco<br>e asciutto</p>

  <p class="block batch">L.SH20 - 001-PES-D.<br>PROD.22-04-2022<br>D.SC.21-04-2024</p>

  <p class="more-title">PROVA ALTRI GUSTI:</p>
  <div class="flavour-art art-fruity" role="img" aria-label="Illustrazione di frutta mista con spruzzi"></div>
  <p class="flavour-label label-fruity">Juicy<br>Blast</p>
  <div class="flavour-art art-tobacco" role="img" aria-label="Illustrazione di foglia di tabacco"></div>
  <p class="flavour-label label-tobacco">Tobacco</p>
  <div class="flavour-art art-vanilla" role="img" aria-label="Illustrazione di fiore e baccelli di vaniglia"></div>
  <p class="flavour-label label-vanilla">Velvet<br>Vanilla</p>

  <div class="hero-art" role="img" aria-label="Illustrazione di foglie di menta"></div>
  <p class="flavour-name">Mystic Mint</p>

  <p class="block producer">PRODOTTO<br>E CONFEZIONATO<br>DA Nordvale srl<br>Via Lario 18<br>20121 Milano<br>P.i.00000000000<br>Tel. +39 000 0000000<br>info@nordvale.it</p>

  <div class="badge badge-collect" style="top:734px">RACCOLTA<br>PLASTICA</div>
  <p class="part" style="top:752px">ETICHETTA</p>
  <div class="badge badge-code" style="top:800px">PAP 5</div>
  <div class="badge badge-collect" style="top:858px">RACCOLTA<br>PLASTICA</div>
  <p class="part" style="top:876px">FLACONE</p>
  <div class="badge badge-code" style="top:925px">PET 1</div>

  <p class="volume">20ML NET</p>

  <svg class="icon" style="left:994px;top:1026px" width="86" height="82" viewBox="0 0 86 82" role="img" aria-label="Riciclabile">
    <defs>
      <marker id="arrow-head" viewBox="0 0 10 10" refX="5" refY="5" markerWidth="3.4" markerHeight="3.4" orient="auto">
        <path d="M0 0 L10 5 L0 10 z" fill="#fff"/>
      </marker>
    </defs>
    <g fill="none" stroke="#fff" stroke-width="5" stroke-linecap="round" marker-end="url(#arrow-head)">
      <path d="M13 58 L34 20"/>
      <path d="M50 18 L71 56"/>
      <path d="M66 74 L22 74"/>
    </g>
  </svg>
  <svg class="icon" style="left:1089px;top:999px" width="86" height="112" viewBox="0 0 86 112" fill="#fff" aria-label="Getta nel contenitore" role="img">
    <circle cx="64" cy="10" r="9"/>
    <path d="M54 24 h20 v44 h-6 v40 h-8 v-40 h-6 z"/>
    <path d="M54 28 L36 44 L40 48 L56 36 z"/>
    <path d="M4 52 h40 l-6 56 h-28 z M12 60 l4 40 h4 l-2 -40 z M28 60 l-2 40 h4 l4 -40 z" fill-rule="evenodd"/>
  </svg>
</main>
</body>
</html>
```